Consulting company needs website design

We need a simple, static website design for our consulting company. We are looking for a general design of the look and feel of the website. Initially, it will have these pages:
- Home
- About us
- Services
- Contact us
We have our own logo which I have attached to the brief.

We are looking for a simple website, with white background and the use of gray (darker) as the main theme. Simple fonts. The website should be responsive so it an be easily red in mobile devices.

As part of the project, we will need to receive at least the following items:
- Individual files with sample text to support the pages outlined above
- Necessary CSS files

Our current website is here: http://www.marlowvane.co/

Here are some examples of other website we like to be used as guideline:
- http://www.tornaviamundo.com/
-

Target Market(s)

Individuals and companies looking to hire our company to provide consulting services.

Industry/Entity Type

It Company

Coding

Coded - Design and coding required

Number of Pages Required

4 page

Font styles to use
Sans Serif

Requirements
Must have
• Main page should have the ability to embed Chirply feed into it.
• We prefer the design to use gray tones.

```html
<!DOCTYPE html>
<html lang="en">
<head>
<meta charset="utf-8">
<title>Marlow Vane Group — Business Improvement Specialists</title>
<link rel="stylesheet" href="https://fonts.googleapis.com/css2?family=Montserrat:wght@300;400;500&family=Open+Sans:wght@400&family=Arimo:ital,wght@0,400;1,400&display=swap">
<style>
:root{
  --ink:#1d1d1d;
  --text:#555555;
  --muted:#8a8a8a;
  --rule:#cfcfcf;
  --dot:#8d8d8d;
  --sky-top:#d9f3fb;
  --sky-mid:#5cb9e8;
  --sky-deep:#1769c4;
  --footer:#333333;
  --footer-field:#4a4a4a;
  --bar:#efefef;
  --white:#ffffff;
  --navy:#1b3d63;
}
*{box-sizing:border-box;margin:0;padding:0}
html,body{width:1200px;height:2242px;overflow:hidden;background:var(--white)}
body{position:relative;font-family:"Arimo",Arial,sans-serif;color:var(--text)}

/* hero */
.hero{position:absolute;left:0;top:0;width:1200px;height:677px;
  background:radial-gradient(ellipse 70% 60% at 55% 15%,var(--sky-top) 0%,var(--sky-mid) 55%,var(--sky-deep) 100%)}
.hero-ridge{position:absolute;left:0;top:560px;width:1200px;height:118px}
.hero-art{position:absolute;left:486px;top:0;width:640px;height:620px;border-radius:40% 20% 30% 30%;
  background:radial-gradient(ellipse at 45% 55%,rgba(30,30,30,.55) 0%,rgba(40,110,190,.35) 45%,rgba(255,255,255,0) 70%)}
.brand{position:absolute;left:80px;top:20px;display:flex;align-items:center;gap:14px}
.brand-mark{width:98px;height:98px;border-radius:50%;background:var(--white);border:3px solid #d6d6d6}
.brand-name{font-family:"Open Sans",sans-serif;font-size:31px;line-height:38px;color:#4d5358}
.nav{position:absolute;top:42px;left:606px;display:flex;align-items:center}
.nav a{font-family:"Montserrat",sans-serif;font-size:15px;color:var(--ink);text-decoration:none;letter-spacing:.3px}
.nav .current{background:#2f2f2f;color:var(--white);border-radius:7px;width:72px;height:52px;display:flex;align-items:center;justify-content:center;margin-right:55px}
.nav .item{margin-right:60px}
.hero-title{position:absolute;left:80px;top:292px;font-family:"Montserrat",sans-serif;font-weight:300;font-size:66px;line-height:74px;color:var(--white)}

/* sections */
.section-title{position:absolute;left:0;width:1200px;text-align:center;font-family:"Montserrat",sans-serif;font-weight:400;font-size:40px;letter-spacing:1px;color:var(--ink)}
.section-title .soft,.side-title .soft{color:#5d5d5d;font-weight:300}
.service{position:absolute;top:800px;width:250px;text-align:center}
.service-ring{width:170px;height:170px;margin:0 auto;border-radius:50%;background:#f4f4f4;border:7px solid #f9f9f9;box-shadow:0 0 0 2px #ececec;display:flex;align-items:center;justify-content:center}
.service-icon{width:90px;height:90px;border-radius:50%;background:#e3e3e3}
.service h3{font-family:"Montserrat",sans-serif;font-weight:400;font-size:21px;color:var(--ink);margin-top:22px}
.service p{font-size:14.5px;line-height:23px;margin-top:8px;color:var(--text)}
.service .more{display:block;margin-top:12px;font-size:15px;color:var(--ink);text-decoration:none}

.divider{position:absolute;left:202px;width:796px;height:10px}
.divider::before{content:"";position:absolute;left:5px;right:5px;top:4px;height:1px;background:var(--rule)}
.divider::after{content:"";position:absolute;left:0;top:0;width:10px;height:10px;border-radius:50%;background:var(--dot);box-shadow:786px 0 0 var(--dot)}

.side-title{position:absolute;font-family:"Montserrat",sans-serif;font-weight:400;font-size:30px;color:var(--ink)}
.about-copy{position:absolute;left:80px;top:1333px;width:650px;font-size:14.5px;line-height:23px}
.about-list{position:absolute;left:80px;top:1457px;list-style:none;font-size:14.5px;line-height:23px}
.about-list li::before{content:"› "}

.tweets{position:absolute;left:792px;top:1282px;width:332px}
.tweets-head{position:absolute;left:0;top:44px;font-size:14.5px;color:var(--muted)}
.tweets-head b{color:var(--ink);font-weight:400}
.tweets-avatar{position:absolute;right:2px;top:0;width:58px;height:58px;border-radius:50%;background:#efefef;border:2px solid #ddd}
.tweets-rule{position:absolute;left:0;top:72px;width:332px;height:1px;background:var(--rule)}
.tweet{position:absolute;left:0;width:332px;font-size:14.5px;line-height:21px;color:var(--text)}
.tweet time{display:block;font-style:italic;font-size:12px;color:var(--muted);margin-top:2px}
.tweets-follow{position:absolute;left:0;top:345px;font-style:italic;font-size:12px;color:var(--ink);text-decoration:underline}

.clients{position:absolute;left:80px;top:1827px;width:1040px;display:flex;justify-content:space-between;align-items:center;height:60px}
.client{font-family:"Montserrat",sans-serif;font-size:17px;color:#aaaaaa;text-align:center;line-height:20px}
.client.dark{color:var(--navy)}

/* footer */
.footer{position:absolute;left:0;top:1939px;width:1200px;height:238px;background:var(--footer);color:var(--white)}
.footer h4{position:absolute;top:32px;font-family:"Montserrat",sans-serif;font-weight:400;font-size:19px;letter-spacing:.5px}
.map{position:absolute;left:78px;top:72px;width:240px;height:125px;background:linear-gradient(135deg,#d9d7d2,#ecebe7 55%,#d4d2cc)}
.contact-row{position:absolute;left:345px;display:flex;gap:14px;font-size:14.5px;line-height:23px}
.contact-row svg{flex:none;margin-top:3px}
.news-field{position:absolute;left:607px;top:72px;width:250px;height:45px;border-radius:6px;background:var(--footer-field);color:#d0d0d0;font-size:14px;padding:13px 20px}
.news-button{position:absolute;left:722px;top:130px;width:135px;height:44px;border-radius:6px;background:var(--white);color:var(--ink);font-family:"Montserrat",sans-serif;font-size:17px;display:flex;align-items:center;justify-content:center}
.footer-mark{position:absolute;left:935px;top:28px;width:126px;height:126px;border-radius:50%;background:#f2f2f2}
.social{position:absolute;top:175px;width:34px;height:34px;border-radius:50%;background:#4f4f4f;color:var(--white);font-family:"Arimo",sans-serif;font-size:15px;text-decoration:none;display:flex;align-items:center;justify-content:center}
.social.first{background:var(--white);color:var(--ink)}
.bottom-bar{position:absolute;left:0;top:2177px;width:1200px;height:65px;background:var(--bar);text-align:center;line-height:65px;font-family:"Montserrat",sans-serif;font-size:13px;color:#777}
.bottom-bar b{color:var(--ink);font-weight:500}
</style>
</head>
<body>

<header class="hero">
  <div class="hero-art" role="img" aria-label="Hand lifting a bar on a 3D bar chart rising from a tablet"></div>
  <svg class="hero-ridge" viewBox="0 0 1200 118" preserveAspectRatio="none" aria-hidden="true">
    <polygon fill="#ffffff" points="0,118 0,60 78,70 110,30 175,60 240,50 300,65 365,52 405,80 470,35 530,60 600,40 660,68 740,48 820,72 890,30 960,66 1040,50 1090,60 1110,25 1140,70 1200,60 1200,118"/>
  </svg>
  <div class="brand">
    <div class="brand-mark"></div>
    <div class="brand-name">Marlow Vane<br>Group</div>
  </div>
  <nav class="nav">
    <a class="current" href="#">HOME</a>
    <a class="item" href="#">ABOUT US</a>
    <a class="item" href="#">SERVICES</a>
    <a href="#">CONTACT US</a>
  </nav>
  <h1 class="hero-title">Business<br>Improvement<br>Specialists</h1>
</header>

<h2 class="section-title" style="top:726px"><span class="soft">OUR</span> SERVICES...</h2>

<div class="service" style="left:80px">
  <div class="service-ring"><div class="service-icon" role="img" aria-label="Light bulb icon"></div></div>
  <h3>Business Strategy</h3>
  <p>Lorem Ipsum is simply dummy text of the printing and typesetting industry. Lorem Ipsum has been the industry's standard dummy text ever since.</p>
  <a class="more" href="#">LEARN MORE</a>
</div>
<div class="service" style="left:343px">
  <div class="service-ring"><div class="service-icon" role="img" aria-label="Team hierarchy icon"></div></div>
  <h3>Management</h3>
  <p>Lorem Ipsum is simply dummy text of the printing and typesetting industry. Lorem Ipsum has been the industry's standard dummy text ever since.</p>
  <a class="more" href="#">LEARN MORE</a>
</div>
<div class="service" style="left:607px">
  <div class="service-ring"><div class="service-icon" role="img" aria-label="Presentation to a group icon"></div></div>
  <h3>Executive Coaching</h3>
  <p>Lorem Ipsum is simply dummy text of the printing and typesetting industry. Lorem Ipsum has been the industry's standard dummy text ever since.</p>
  <a class="more" href="#">LEARN MORE</a>
</div>
<div class="service" style="left:872px">
  <div class="service-ring"><div class="service-icon" role="img" aria-label="Network of connections icon"></div></div>
  <h3>Business Development</h3>
  <p>Lorem Ipsum is simply dummy text of the printing and typesetting industry. Lorem Ipsum has been the industry's standard dummy text ever since.</p>
  <a class="more" href="#">LEARN MORE</a>
</div>

<div class="divider" style="top:1211px"></div>

<h2 class="side-title" style="left:80px;top:1280px"><span class="soft">ABOUT</span> US</h2>
<p class="about-copy">Lorem Ipsum is simply dummy text of the printing and typesetting industry. Lorem Ipsum has been the industry's standard dummy text ever since the 1500s, when an unknown printer took a galley of type and scrambled it to make a type specimen book. It has survived not only five centuries, but also the leap into electronic typesetting, remaining essentially unchanged. It was popularised in the 1960s with the release of transfer sheets containing Lorem Ipsum passages</p>
<ul class="about-list">
  <li>Business Strategy</li>
  <li>Executive Coaching</li>
  <li>Corporate Governance</li>
  <li>Performance Management</li>
  <li>Interim Management of Special Projects</li>
  <li>New Business Development</li>
  <li>Risk Management</li>
  <li>Financial Management</li>
</ul>

<section class="tweets">
  <h2 class="side-title" style="left:0;top:0"><span class="soft">RECENT</span> TWEETS</h2>
  <div class="tweets-avatar"></div>
  <div class="tweets-head"><b>Marlow Vane</b> @MarlowVane</div>
  <div class="tweets-rule"></div>
  <p class="tweet" style="top:80px">Great insights about #data and #analytics at the Northfield Data Quality Symposium http://shrt.ly/4kqPw2 &nbsp;http://shrt.ly/7nTe9c<time>about 4 hours ago</time></p>
  <p class="tweet" style="top:175px">"Future proofing," your #Analytics / #Data Science skills<time>about 13 hours ago</time></p>
  <p class="tweet" style="top:248px">“if we cannot get the basics right then we cannot possibly pull off the fancy plays it takes to win the games”<time>about 2 weeks ago</time></p>
  <a class="tweets-follow" href="#">Follow on Chirply</a>
</section>

<div class="divider" style="top:1691px"></div>

<h2 class="section-title" style="top:1749px"><span class="soft">OUR</span> CLIENTS...</h2>
<div class="clients">
  <span class="client dark">Fetchwise</span>
  <span class="client">Eastvale State<br>University</span>
  <span class="client">Corvin Hale<br>Media</span>
  <span class="client">University<br>of Larkmoor</span>
  <span class="client">Telvora</span>
  <span class="client">The Summit<br>Council</span>
</div>

<footer class="footer">
  <h4 style="left:80px">LOCATION</h4>
  <div class="map" role="img" aria-label="Street map of the office location"></div>

  <h4 style="left:345px">CONTACT INFO</h4>
  <div class="contact-row" style="top:70px">
    <svg width="16" height="20" viewBox="0 0 16 20" aria-hidden="true"><path fill="#fff" d="M8 0a7 7 0 0 0-7 7c0 5 7 13 7 13s7-8 7-13a7 7 0 0 0-7-7zm0 9.5A2.5 2.5 0 1 1 8 4.5a2.5 2.5 0 0 1 0 5z"/></svg>
    <span>123 Building Name, Street,<br>City, Country - Zip code</span>
  </div>
  <div class="contact-row" style="top:136px">
    <svg width="16" height="16" viewBox="0 0 16 16" aria-hidden="true"><path fill="#fff" d="M3.5 0.5l2.5 3-1.6 2c.9 2 2.6 3.7 4.6 4.6l2-1.6 3 2.5-1.6 3C6 13.5 2.5 10 0.5 2.1z"/></svg>
    <span>123-4567-890</span>
  </div>
  <div class="contact-row" style="top:176px">
    <svg width="18" height="14" viewBox="0 0 18 14" aria-hidden="true"><rect width="18" height="14" rx="2" fill="#fff"/><path d="M1 2l8 6 8-6" fill="none" stroke="#333" stroke-width="1.5"/></svg>
    <span>info@marlowvanegroup.com</span>
  </div>

  <h4 style="left:609px">NEWSLETTER</h4>
  <div class="news-field">Enter Your E-Mail...</div>
  <div class="news-button">SUBSCRIBE</div>

  <div class="footer-mark"></div>
  <a class="social first" style="left:938px" href="#" aria-label="Pagebook">P</a>
  <a class="social" style="left:980px" href="#" aria-label="Chirply">C</a>
  <a class="social" style="left:1021px" href="#" aria-label="Linkwork">L</a>
</footer>

<div class="bottom-bar">© <b>MARLOW VANE GROUP</b> – 2016. All Rights Reserved.</div>

</body>
</html>
```